Stationery Design needed for logo design project

This company needs a letterhead and envelope for their new practice. We did not want to release this contact until the business card design was finalized so the stationary can be created to coordinate with it.

For those of you that will be submitting designs for this content, think "linear". Designs with curves or "swooshes" are not appropriate for this design.

NOTE: As part of the source files; I will require FULLY LAYERED PHOTOSHOP FILES of all elements, including design elements, text and fonts. If you cannot provide a fully layered PSD file, please do not submit.
Updates

The project details have been updated. We have added a new description along with logo files and business card design. Please review the style of the logo and business card before submitting designs. Thanks

Target Market(s)

Medical

Industry/Entity Type

Business

Requirements
Must have
• NOTE: As part of the source files; I will require FULLY LAYERED PHOTOSHOP FILES of all elements, including design elements, text and fonts. If you cannot provide a fully layered PSD file, please do not submit.

Logo
2 office address locations
phone
fax
email
website URL

```html
<!DOCTYPE html>
<html lang="en">
<head>
<meta charset="utf-8">
<title>Marlow &amp; Associates Stationery</title>
<link rel="stylesheet" href="https://fonts.googleapis.com/css2?family=Fira+Sans+Condensed:wght@400;600&family=Tinos&display=swap">
<style>
:root{
  --red:#a81c25;
  --black:#111;
  --ink:#333;
  --muted:#666;
  --stage:#e9ebed;
  --paper:#fff;
  --field:#eceff1;
  --window:#e6e7e9;
}
*{box-sizing:border-box;margin:0;padding:0}
html,body{width:1200px;height:524px;overflow:hidden;background:var(--stage)}
body{position:relative;font-family:"Fira Sans Condensed",Arial,sans-serif;color:var(--ink)}
.sheet{position:absolute;background:var(--paper);box-shadow:0 1px 5px rgba(0,0,0,.25);overflow:hidden}

/* envelope back */
.envelope-back{left:27px;top:37px;width:378px;height:208px}
.envelope-back .flap{position:absolute;left:0;top:0;width:100%;height:60px;background:var(--red)}
.envelope-back .flap-dot{position:absolute;left:183px;top:18px;width:22px;height:22px;border-radius:50%;background:var(--paper)}

/* brand */
.brand{position:absolute;display:flex;align-items:center;gap:6px;white-space:nowrap}
.brand-dot{border-radius:50%;background:var(--red);flex:none}
.brand-name{font-weight:400;color:var(--black);letter-spacing:.5px}

/* envelope front */
.envelope-front{left:27px;top:252px;width:378px;height:214px}
.envelope-front .brand{left:24px;top:52px}
.envelope-front .brand-dot{width:18px;height:18px}
.envelope-front .brand-name{font-size:15px}
.addresses{position:absolute;left:22px;top:114px;font-size:7.2px;line-height:9.2px;color:var(--black)}
.addresses h4{color:var(--red);font-weight:600;font-size:7.4px}
.addresses p+h4{margin-top:4px}
.window{position:absolute;left:173px;top:107px;width:171px;height:53px;border-radius:6px;background:var(--window)}

.band-red{position:absolute;left:0;bottom:0;width:100%;height:6px;background:var(--red)}
.band-black{position:absolute;bottom:0;background:var(--black)}
.envelope-front .band-black{left:200px;width:178px;height:11px}

/* letter pages */
.letterhead{left:432px;top:12px;width:353px;height:500px}
.fax{left:819px;top:16px;width:353px;height:496px}
.page .brand{left:50%;transform:translateX(-50%);top:36px}
.page .brand-dot{width:20px;height:20px}
.page .brand-name{font-size:19px}
.salutation{position:absolute;left:26px;top:108px;font-size:6.5px;line-height:7.2px;color:var(--ink)}
.body{position:absolute;left:26px;width:300px;font-size:6.7px;line-height:8.2px;color:var(--muted);text-align:justify}
.body p+p{margin-top:7px}
.body .serif{font-family:Tinos,"Times New Roman",serif;font-size:6.5px;line-height:8.4px}
.signature{position:absolute;left:26px;width:62px;height:22px;background:linear-gradient(90deg,#eee,#f7f7f7);border-radius:3px}

.contact{position:absolute;left:26px;font-size:6.6px;line-height:8.6px;color:var(--black)}
.contact li{list-style:none;display:flex;align-items:center;gap:4px}
.contact svg{width:5px;height:5px;fill:var(--red)}
.office{position:absolute;font-size:6.6px;line-height:7.8px;color:var(--black)}
.office h4{color:var(--red);font-weight:600;font-size:6.8px;margin-bottom:1px}
.page .band-red{height:5px}
.page .band-black{left:188px;width:165px;height:16px}

/* fax form */
.fax-table{position:absolute;left:22px;top:96px;width:306px;border-collapse:separate;border-spacing:2px 1px;font-size:5.8px;color:var(--black)}
.fax-table th{font-weight:400;text-align:left;width:40px;height:15px;padding-left:2px;background:var(--field)}
.fax-table td{background:var(--field);width:106px}
.checks{position:absolute;left:24px;top:166px;display:flex;gap:12px;font-size:5.4px;color:var(--black)}
.checks span{display:flex;align-items:center;gap:3px}
.checks i{display:inline-block;width:6px;height:6px;border:.6px solid #555}
</style>
</head>
<body>

<section class="sheet envelope-back" aria-label="Envelope back">
  <div class="flap"><div class="flap-dot"></div></div>
</section>

<section class="sheet envelope-front" aria-label="Envelope front">
  <div class="brand"><span class="brand-dot"></span><span class="brand-name">Marlow &amp; Associates</span></div>
  <div class="addresses">
    <h4>Downtown Office:</h4>
    <p>412 Cedar Ridge Ave<br>Suite 14<br>Fairview, NM 87010</p>
    <h4>West Side Office:</h4>
    <p>88 Mesa Vista Rd<br>Suite 305<br>Fairview, NM 87011</p>
  </div>
  <div class="window"></div>
  <div class="band-red"></div>
  <div class="band-black"></div>
</section>

<section class="sheet page letterhead" aria-label="Letterhead">
  <div class="brand"><span class="brand-dot"></span><span class="brand-name">Marlow &amp; Associates</span></div>
  <p class="salutation">Lpsum, lorem<br>dolor sit amet<br>Lorem, dummy text</p>
  <div class="body" style="top:146px">
    <p>Lorem ipsum dolor sit amet, consetetur sadipscing elitr, sed diam nonumy eirmod tempor invidunt ut labore et dolore magna aliquyam erat, sed diam voluptua. At vero eos et accusam et justo duo dolores et ea rebum. Stet clita kasd gubergren, no sea takimata sanctus est Lorem ipsum dolor sit</p>
    <p>Lorem ipsum dolor sit amet, consetetur sadipscing elitr, sed diam nonumy eirmod tempor invidunt ut labore et dolore magna aliquyam erat, sed diam voluptua. At vero eos et accusam et justo duo dolores et ea rebum. Stet clita kasd gubergren, no sea takimata sanctus est Lorem ipsum dolor sit amet. Lorem ipsum dolor sit amet, consetetur sadipscing elitr, sed diam nonumy eirmod tempor invidunt ut labore et dolore magna aliquyam erat, sed diam voluptua. At vero eos et accusam et justo duo dolores et ea rebum. Stet clita kasd gubergren, no sea takimata sanctus est Lorem ipsum dolor sit amet. Lorem ipsum dolor sit amet, consetetur sadipscing elitr, sed diam nonumy eirmod tempor invidunt ut labore et dolore magna aliquyam erat, sed diam voluptua. At vero eos et accusam et justo duo dolores et ea rebum. Stet clita kasd gubergren, no sea takimata sanctus est</p>
    <p class="serif">Duis autem vel eum iriure dolor in hendrerit in vulputate velit esse molestie consequat, vel illum dolore eu feugiat nulla facilisis at vero eros et accumsan et iusto odio dignissim qui blandit praesent luptatum zzril delenit augue duis dolore te feugait nulla facilisi. Lorem ipsum dolor sit amet, consectetuer adipiscing elit, sed diam nonummy nibh euismod tincidunt ut laoreet dolore magna aliquam erat volutpat.</p>
    <p class="serif">Ut wisi enim ad minim veniam, quis nostrud exerci tation ullamcorper suscipit lobortis nisl ut aliquip ex ea commodo consequat. Duis autem vel eum iriure dolor in hendrerit in vulputate velit esse molestie consequat, vel illum dolore eu feugiat nulla facilisis at vero eros et accumsan et iusto odio dignissim qui blandit praesent luptatum zzril delenit augue duis dolore te feugait nulla facilisi.</p>
  </div>
  <div class="signature" style="top:380px" role="img" aria-label="Handwritten signature"></div>
  <ul class="contact" style="top:434px">
    <li><svg viewBox="0 0 10 10"><circle cx="5" cy="5" r="5"/></svg>(555) 201-4410</li>
    <li><svg viewBox="0 0 10 10"><circle cx="5" cy="5" r="5"/></svg>(555) 201-4411</li>
    <li><svg viewBox="0 0 10 10"><circle cx="5" cy="5" r="5"/></svg>nora@marlowcardio.example</li>
    <li><svg viewBox="0 0 10 10"><circle cx="5" cy="5" r="5"/></svg>www.marlowcardio.example</li>
  </ul>
  <div class="office" style="left:136px;top:436px"><h4>West Side Office:</h4><p>88 Mesa Vista Rd<br>Suite 305<br>Fairview, NM 87011</p></div>
  <div class="office" style="left:256px;top:432px"><h4>Downtown Office:</h4><p>412 Cedar Ridge Ave<br>Suite 14<br>Fairview, NM 87010</p></div>
  <div class="band-red"></div>
  <div class="band-black"></div>
</section>

<section class="sheet page fax" aria-label="Fax cover sheet">
  <div class="brand"><span class="brand-dot"></span><span class="brand-name">Marlow &amp; Associates</span></div>
  <table class="fax-table">
    <tr><th>To</th><td></td><th>From</th><td></td></tr>
    <tr><th>FAX</th><td></td><th>Pages</th><td></td></tr>
    <tr><th>Phone</th><td></td><th>Date</th><td></td></tr>
    <tr><th>Re</th><td></td><th>CC</th><td></td></tr>
  </table>
  <div class="checks">
    <span><i></i>Urgent</span><span><i></i>For Review</span><span><i></i>Please comment</span><span><i></i>Please reply</span><span><i></i>Please recycle</span>
  </div>
  <div class="body" style="top:206px">
    <p>Lorem ipsum dolor sit amet, consetetur sadipscing elitr, sed diam nonumy eirmod tempor invidunt ut labore et dolore magna aliquyam erat, sed diam voluptua. At vero eos et accusam et justo duo dolores et ea rebum. Stet clita kasd gubergren, no sea takimata sanctus est Lorem ipsum dolor sit</p>
    <p>Lorem ipsum dolor sit amet, consetetur sadipscing elitr, sed diam nonumy eirmod tempor invidunt ut labore et dolore magna aliquyam erat, sed diam voluptua. At vero eos et accusam et justo duo dolores et ea rebum. Stet clita kasd gubergren, no sea takimata sanctus est Lorem ipsum dolor sit amet. Lorem ipsum dolor sit amet, consetetur sadipscing elitr, sed diam nonumy eirmod tempor invidunt ut labore et dolore magna aliquyam erat, sed diam voluptua. At vero eos et accusam et justo duo dolores et ea rebum. Stet clita kasd gubergren, no sea takimata sanctus est Lorem ipsum dolor sit amet. Lorem ipsum dolor sit amet, consetetur sadipscing elitr, sed diam nonumy eirmod tempor invidunt ut labore et dolore magna aliquyam erat, sed diam voluptua. At vero eos et accusam et justo duo dolores et ea rebum. Stet clita kasd gubergren, no sea takimata sanctus est</p>
    <p class="serif">Duis autem vel eum iriure dolor in hendrerit in vulputate velit esse molestie consequat, vel illum dolore eu feugiat nulla facilisis at vero eros et accumsan et iusto odio dignissim qui blandit praesent luptatum zzril delenit augue duis dolore te feugait nulla facilisi. Lorem ipsum dolor sit amet, consectetuer adipiscing elit, sed diam nonummy nibh euismod tincidunt ut laoreet dolore magna aliquam erat volutpat.</p>
  </div>
  <div class="signature" style="top:382px" role="img" aria-label="Handwritten signature"></div>
  <ul class="contact" style="top:430px">
    <li><svg viewBox="0 0 10 10"><circle cx="5" cy="5" r="5"/></svg>(555) 201-4410</li>
    <li><svg viewBox="0 0 10 10"><circle cx="5" cy="5" r="5"/></svg>(555) 201-4411</li>
    <li><svg viewBox="0 0 10 10"><circle cx="5" cy="5" r="5"/></svg>nora@marlowcardio.example</li>
    <li><svg viewBox="0 0 10 10"><circle cx="5" cy="5" r="5"/></svg>www.marlowcardio.example</li>
  </ul>
  <div class="office" style="left:135px;top:432px"><h4>West Side Office:</h4><p>88 Mesa Vista Rd<br>Suite 305<br>Fairview, NM 87011</p></div>
  <div class="office" style="left:255px;top:428px"><h4>Downtown Office:</h4><p>412 Cedar Ridge Ave<br>Suite 14<br>Fairview, NM 87010</p></div>
  <div class="band-red"></div>
  <div class="band-black"></div>
</section>

</body>
</html>
```